Quartz Meridian Business Card Design

I need a 2-sided business card for my computer engineering consulting company. The card is expected to convey a message of cutting edge forward thinking, and boldnes. I would like the card to be memorable and stand-out on a desk. The card should be bold, modern, clean, and highly professional. I am a big fan of watermarks/shadows and other intersting but restrained uses of the logo. The card can be a shape other than the traditional rectangle. Perhaps a rectangle with rounded edges. All I ask is the card be able to fit into a standard wallet. I will supply two logos, one with a red background, and one with a black background. Please feel free to work with both of these logos.
Updates

Hi all, thank you for your submissions. I will post the original vector file later today. Thank you for your patience.

Regards,

Henry

Target Market(s)

Engineering Buyers, Vice Presidents and Directors

Industry/Entity Type

Computer

Requirements
Must have
• 2 sides

```html
<!DOCTYPE html>
<html lang="en">
<head>
<meta charset="utf-8">
<title>Quartz Meridian Works – Business Card</title>
<link rel="stylesheet" href="https://fonts.googleapis.com/css2?family=Questrial&display=swap">
<style>
  :root {
    --page-bg: #dfe4e6;
    --card-white: #ffffff;
    --card-dark: #2f2f2f;
    --card-back: #262626;
    --brand-red: #c4262e;
    --brand-grey: #4a4a4a;
    --tagline-grey: #8a8a8a;
    --text-light: #f2f2f2;
    --text-muted: #bdbdbd;
    --watermark: rgba(255,255,255,0.035);
  }
  * { box-sizing: border-box; margin: 0; padding: 0; }
  html, body {
    width: 1200px; height: 960px; overflow: hidden;
    background: var(--page-bg);
    font-family: "Questrial", "Century Gothic", sans-serif;
  }
  .sheet {
    width: 1200px; height: 960px;
    display: flex; flex-direction: column;
    align-items: center; justify-content: center; gap: 52px;
  }
  .card {
    width: 700px; height: 400px;
    border-radius: 6px; overflow: hidden; position: relative;
    box-shadow: 0 6px 18px rgba(0,0,0,0.18);
  }

  /* Front */
  .card--front { background: var(--card-dark); }
  .front__brand {
    height: 182px; background: var(--card-white);
    display: flex; flex-direction: column; align-items: center; justify-content: center;
    border-bottom: 3px solid var(--brand-red);
    box-shadow: 0 4px 0 var(--card-white);
  }
  .brand-mark { display: flex; align-items: center; gap: 12px; }
  .brand-mark__square { width: 22px; height: 22px; background: var(--brand-red); flex: none; }
  .brand-mark__name {
    font-size: 28px; letter-spacing: 0.5px; color: var(--brand-grey);
    text-transform: uppercase; white-space: nowrap;
  }
  .brand-tagline {
    margin-top: 6px; font-size: 12px; letter-spacing: 3px;
    color: var(--tagline-grey); text-transform: uppercase; white-space: nowrap;
  }
  .front__person { text-align: center; margin-top: 30px; color: var(--text-light); }
  .person__name { font-size: 34px; font-weight: 400; }
  .person__title { font-size: 18px; margin-top: 6px; color: var(--text-muted); }
  .front__contacts {
    position: absolute; left: 40px; right: 30px; bottom: 36px;
    display: grid; grid-template-columns: 250px 1fr; row-gap: 10px; column-gap: 20px;
  }
  .contact { display: flex; align-items: center; gap: 8px; color: var(--text-light); font-size: 17px; white-space: nowrap; }
  .contact__icon {
    width: 20px; height: 20px; border-radius: 3px; background: var(--brand-red);
    color: #fff; font-size: 14px; line-height: 19px; text-align: center; flex: none;
  }

  /* Back */
  .card--back {
    background: linear-gradient(160deg, #333333 0%, var(--card-back) 55%, #1f1f1f 100%);
  }
  .back__watermark {
    position: absolute; left: 80px; top: -20px;
    width: 300px; height: 300px; border-radius: 50%;
    background: var(--watermark);
  }
  .back__brand {
    position: absolute; right: 36px; bottom: 40px; text-align: right;
  }
  .back__brand .brand-mark { justify-content: flex-end; gap: 10px; }
  .back__brand .brand-mark__square { width: 16px; height: 16px; }
  .back__brand .brand-mark__name { font-size: 22px; color: var(--text-light); }
  .back__brand .brand-tagline { font-size: 11px; color: var(--text-muted); margin-top: 4px; }
</style>
</head>
<body>
<main class="sheet">

  <section class="card card--front" aria-label="Business card front">
    <header class="front__brand">
      <div class="brand-mark">
        <span class="brand-mark__square"></span>
        <span class="brand-mark__name">Quartz Meridian Works</span>
      </div>
      <p class="brand-tagline">Precision Built Forward</p>
    </header>
    <div class="front__person">
      <h1 class="person__name">Sam Porter</h1>
      <p class="person__title">IT Director</p>
    </div>
    <div class="front__contacts">
      <p class="contact"><span class="contact__icon">t</span>0123 456 7890 ext 2210</p>
      <p class="contact"><span class="contact__icon">e</span>sam.porter@qmworks.com</p>
      <p class="contact"><span class="contact__icon">w</span>www.qmworks.com</p>
      <p class="contact"><span class="contact__icon">a</span>The Studio, The Quay, The City, QM2 7HT</p>
    </div>
  </section>

  <section class="card card--back" aria-label="Business card back">
    <span class="back__watermark"></span>
    <div class="back__brand">
      <div class="brand-mark">
        <span class="brand-mark__square"></span>
        <span class="brand-mark__name">Quartz Meridian Works</span>
      </div>
      <p class="brand-tagline">Precision Built Forward</p>
    </div>
  </section>

</main>
</body>
</html>
```